Pilates Classes Flyer Design

I need a flyer designed that will promote my range of classes held in Bath, UK. I teach beginners, intermediate level and Over 50's and 60's and also teach individuals in their own homes. I would like to see designs using my colours blue Pantone 306 and Lime Green 14-0452 TPX TCX. The flyer should reflect a friendly, welcoming and professional class structure. I attach an old flyer for your reference and copy.

Target Market(s)

Men and Women who have busy lives working hard, who recognise they need to stretch out, do some exercise and de-stress after a busy day

Ladies over 50 who want to do some Pilates in a friendly fun environment and meet people at the same time.

Industry/Entity Type

It Professional

Font styles to use
Sans Serif
Script

Requirements
Must have
• One-sided flyer
Text only logo. Drop the figure

```html
<!DOCTYPE html>
<html lang="en">
<head>
<meta charset="utf-8">
<title>Pilates Classes Flyer</title>
<link rel="stylesheet" href="https://fonts.googleapis.com/css2?family=Great+Vibes&family=Cinzel:wght@500;600&family=Open+Sans:wght@400;600;700&display=swap">
<style>
  :root {
    --green-deep: #3f8a2a;
    --green-mid: #7cc043;
    --lime: #b5d84a;
    --sky: #6fb3e0;
    --brand-blue: #0a8fd4;
    --banner-blue: #1d8fd2;
    --panel-teal: #2f6e8c;
    --panel-bg: #eef3e6;
    --ink: #2a2a2a;
    --white: #ffffff;
  }
  html, body {
    margin: 0;
    padding: 0;
    width: 820px;
    height: 1200px;
    overflow: hidden;
    background: #ffffff;
  }
  .flyer {
    position: relative;
    width: 820px;
    height: 1200px;
    overflow: hidden;
    font-family: "Open Sans", Arial, sans-serif;
    color: var(--ink);
  }
  .backdrop {
    position: absolute;
    inset: 0;
    background:
      radial-gradient(circle at 20% 10%, rgba(111,179,224,0.85) 0, rgba(111,179,224,0) 30%),
      radial-gradient(circle at 54% 40%, var(--lime) 0, var(--green-mid) 45%, var(--green-deep) 90%);
  }
  .spotlight {
    position: absolute;
    left: 105px;
    top: 140px;
    width: 680px;
    height: 680px;
    border-radius: 50%;
    background: radial-gradient(circle, #ffffff 0, #fbfdf6 55%, #eaf3dc 80%, rgba(234,243,220,0.6) 100%);
    box-shadow: 0 0 0 8px rgba(10,143,212,0.55), 0 0 40px rgba(255,255,255,0.7);
  }
  .leaves {
    position: absolute;
    left: 600px;
    top: 10px;
    width: 190px;
    height: 130px;
    border-radius: 50%;
    background: radial-gradient(ellipse, rgba(200,230,140,0.9) 0, rgba(200,230,140,0) 70%);
  }
  .figure-photo {
    position: absolute;
    left: 0;
    top: 310px;
    width: 265px;
    height: 820px;
    border-radius: 0 120px 20px 0;
    background: linear-gradient(180deg, rgba(235,220,205,0.85) 0, rgba(190,170,160,0.8) 35%, rgba(60,45,40,0.85) 65%, rgba(55,40,35,0.9) 100%);
  }
  .mat-photo {
    position: absolute;
    left: 0;
    top: 1128px;
    width: 440px;
    height: 34px;
    background: linear-gradient(180deg, #5aa0c8 0, #3d7fa8 100%);
  }
  .title {
    position: absolute;
    left: 150px;
    top: 100px;
    margin: 0;
    font-family: "Great Vibes", cursive;
    font-weight: 400;
    font-size: 200px;
    line-height: 1;
    color: #1e1e1e;
    text-shadow: 2px 3px 4px rgba(0,0,0,0.25);
  }
  .headline {
    position: absolute;
    left: 372px;
    top: 328px;
    margin: 0;
    font-family: "Cinzel", serif;
    font-weight: 600;
    color: var(--brand-blue);
    line-height: 1;
  }
  .headline .line1 { display: block; font-size: 42px; }
  .headline .line2 { display: block; font-size: 32px; margin-left: 22px; margin-top: 2px; }
  .intro {
    position: absolute;
    left: 365px;
    top: 428px;
    width: 390px;
    margin: 0;
    padding-top: 8px;
    border-top: 2px dotted #9aa;
    font-size: 19px;
    line-height: 1.22;
  }
  .intro strong { font-weight: 700; }
  .feature {
    position: absolute;
    display: flex;
    align-items: center;
    gap: 12px;
    height: 46px;
    padding-left: 10px;
    background: linear-gradient(90deg, var(--banner-blue) 0, var(--banner-blue) 75%, rgba(29,143,210,0) 100%);
    color: var(--white);
    font-size: 17px;
    line-height: 1.1;
  }
  .feature svg { flex: none; }
  .feature-one { left: 352px; top: 528px; width: 400px; }
  .feature-two { left: 322px; top: 632px; width: 420px; }
  .feature-note {
    position: absolute;
    margin: 0;
    font-size: 17px;
    line-height: 1.2;
  }
  .note-one { left: 365px; top: 580px; }
  .note-two { left: 305px; top: 686px; }
  .brand-name {
    position: absolute;
    left: 282px;
    top: 766px;
    margin: 0;
    font-size: 30px;
    font-weight: 400;
    color: var(--brand-blue);
  }
  .schedule {
    position: absolute;
    left: 232px;
    top: 918px;
    width: 544px;
    height: 162px;
    border-radius: 12px 12px 4px 4px;
    background: var(--panel-bg);
    overflow: hidden;
    box-shadow: 0 2px 6px rgba(0,0,0,0.25);
  }
  .schedule-title {
    margin: 0;
    height: 42px;
    line-height: 44px;
    text-align: center;
    font-family: "Cinzel", serif;
    font-weight: 500;
    font-size: 25px;
    color: var(--white);
    background: var(--panel-teal);
  }
  .venues {
    display: flex;
    padding: 10px 8px 0;
  }
  .venue {
    flex: 1;
    text-align: center;
    font-size: 13px;
    line-height: 1.3;
  }
  .venue + .venue { border-left: 1px dotted #8aa; }
  .venue-name { color: var(--panel-teal); font-size: 15px; margin: 0 0 4px; }
  .venue-times { margin: 0; }
  .contact {
    position: absolute;
    right: 48px;
    top: 1092px;
    text-align: left;
    color: var(--white);
  }
  .phone {
    display: flex;
    align-items: center;
    gap: 8px;
    margin: 0;
    font-size: 32px;
    font-weight: 700;
    line-height: 1;
  }
  .email {
    margin: 6px 0 0 6px;
    font-size: 17px;
  }
</style>
</head>
<body>
<main class="flyer">
  <div class="backdrop" role="img" aria-label="Blurred green swirl background with soft blue light and floating bubbles"></div>
  <div class="spotlight"></div>
  <div class="leaves" role="img" aria-label="Scattered light green leaves"></div>
  <div class="figure-photo" role="img" aria-label="Photo of a woman holding a standing bow pose"></div>
  <div class="mat-photo" role="img" aria-label="Blue exercise mat"></div>

  <h1 class="title">Pilates</h1>
  <h2 class="headline"><span class="line1">New Classes</span><span class="line2">Near You !</span></h2>
  <p class="intro">Pilates is for <strong>EVERYONE</strong> whatever level of fitness, age or ability to help you build strength, flexibility and overall well-being.</p>

  <div class="feature feature-one">
    <svg width="32" height="32" viewBox="0 0 32 32" aria-hidden="true"><circle cx="16" cy="16" r="13" fill="none" stroke="#fff" stroke-width="3"/><path d="M9 16l5 5 10-11" fill="none" stroke="#fff" stroke-width="3.5" stroke-linecap="round" stroke-linejoin="round"/></svg>
    <span>Quality Teaching with<br>Core Balance Method Teacher</span>
  </div>
  <p class="feature-note note-one">Progressive approach.<br>Teaching good movement skills.</p>

  <div class="feature feature-two">
    <svg width="32" height="32" viewBox="0 0 32 32" aria-hidden="true"><circle cx="16" cy="16" r="13" fill="none" stroke="#fff" stroke-width="3"/><path d="M9 16l5 5 10-11" fill="none" stroke="#fff" stroke-width="3.5" stroke-linecap="round" stroke-linejoin="round"/></svg>
    <span>Small Class Sizes and<br>Friendly Atmosphere</span>
  </div>
  <p class="feature-note note-two">Beginners, Intermediate and<br>Over 50's classes to choose from.</p>

  <p class="brand-name">StillPoint Pilates</p>

  <section class="schedule">
    <h3 class="schedule-title">Join my one-hour classes at</h3>
    <div class="venues">
      <div class="venue">
        <p class="venue-name">St Anne's Church Hall<br>Elm Rise</p>
        <p class="venue-times">Monday Evenings<br>Tuesday Mornings<br>Friday Mornings</p>
      </div>
      <div class="venue">
        <p class="venue-name">Linden Fields<br>Dr. Surgery</p>
        <p class="venue-times">Tuesday evenings</p>
      </div>
      <div class="venue">
        <p class="venue-name">Harcourt Centre,<br>Mill Road,</p>
        <p class="venue-times">Wednesday Mornings<br>Wednesday Evenings.</p>
      </div>
    </div>
  </section>

  <div class="contact">
    <p class="phone">
      <svg width="28" height="28" viewBox="0 0 28 28" aria-hidden="true"><rect width="28" height="28" rx="5" fill="#1d8fd2"/><path d="M9 6c-2 1-3 3-2 6 2 5 5 8 10 10 3 1 5 0 6-2l-3-3-3 2c-2-1-4-3-5-5l2-3z" fill="#fff"/></svg>
      07700900123
    </p>
    <p class="email">tessa.marlow@mailbox.co.uk</p>
  </div>
</main>
</body>
</html>
```